I am a home builder and developer

I would like some sort of architectural design like a pencil type of drawing of a house but want it to be professional looking and two sided.

Simply I am a custom home builder and land developer. I would like a new design other than what I have now that's what I thought y'all did. I like mostly black maybe with an pencil type of drawing of a house. Like an architectural look.

Industry/Entity Type

Home Builder

```html
<!DOCTYPE html>
<html lang="en">
<head>
<meta charset="UTF-8">
<title>Ridgeline Building Inc – Business Card</title>
<link href="https://fonts.googleapis.com/css2?family=Quicksand:wght@500;700&family=Noto+Serif:wght@700&family=Open+Sans:wght@400&display=swap" rel="stylesheet">
<style>
  :root {
    --backdrop: #e9e6e1;
    --card-dark: #1f1e1e;
    --card-light: #ffffff;
    --brand-red: #a3202f;
    --ink: #2b2b2b;
    --muted-grey: #b9b9b9;
  }
  html, body {
    margin: 0;
    padding: 0;
    width: 1200px;
    height: 801px;
    overflow: hidden;
    background: var(--backdrop);
  }
  .canvas {
    position: relative;
    width: 1200px;
    height: 801px;
  }
  .card {
    position: absolute;
    top: 246px;
    width: 540px;
    height: 309px;
    border-radius: 4px;
    box-shadow: 0 6px 18px rgba(0,0,0,0.18);
    box-sizing: border-box;
  }
  .card--front {
    left: 40px;
    background: var(--card-dark);
  }
  .card--back {
    left: 620px;
    background: var(--card-light);
  }
  .brand-mark {
    position: absolute;
    left: 0;
    right: 0;
    text-align: center;
    font-family: "Quicksand", sans-serif;
    font-weight: 700;
    font-size: 30px;
    letter-spacing: 1px;
    color: var(--brand-red);
  }
  .card--front .brand-mark { top: 100px; }
  .card--back .brand-mark { top: 34px; }
  .brand-mark .brand-square {
    display: inline-block;
    width: 14px;
    height: 14px;
    background: var(--brand-red);
    margin-right: 10px;
    vertical-align: 3px;
  }
  .tagline {
    position: absolute;
    top: 168px;
    left: 0;
    right: 0;
    text-align: center;
    font-family: "Open Sans", sans-serif;
    font-size: 16px;
    color: var(--muted-grey);
  }
  .contact-block {
    position: absolute;
    top: 92px;
    left: 0;
    right: 0;
    text-align: center;
  }
  .person-name {
    font-family: "Quicksand", sans-serif;
    font-weight: 500;
    font-size: 27px;
    color: var(--ink);
    margin: 0;
  }
  .person-role {
    font-family: "Noto Serif", serif;
    font-weight: 700;
    font-size: 17px;
    color: var(--brand-red);
    margin: 2px 0 14px;
  }
  .contact-line {
    display: flex;
    justify-content: center;
    align-items: center;
    gap: 10px;
    font-family: "Quicksand", sans-serif;
    font-weight: 700;
    font-size: 16px;
    color: var(--ink);
    margin: 4px 0;
  }
  .contact-line svg { width: 16px; height: 16px; fill: var(--brand-red); }
  .licenses {
    position: absolute;
    bottom: 30px;
    left: 0;
    right: 0;
    text-align: center;
    font-family: "Quicksand", sans-serif;
    font-weight: 500;
    font-size: 18px;
    color: var(--ink);
  }
  .licenses .licenses-label { color: var(--brand-red); margin-right: 12px; }
  .licenses .divider { margin: 0 10px; }
</style>
</head>
<body>
<main class="canvas">
  <section class="card card--front" aria-label="Card front">
    <div class="brand-mark"><span class="brand-square"></span>Ridgeline Building Inc</div>
    <p class="tagline">Custom home builder and land developer</p>
  </section>

  <section class="card card--back" aria-label="Card back">
    <div class="brand-mark"><span class="brand-square"></span>Ridgeline Building Inc</div>
    <div class="contact-block">
      <p class="person-name">Daniel Hartwell</p>
      <p class="person-role">President and Owner</p>
      <div class="contact-line">
        <svg viewBox="0 0 24 24" aria-hidden="true"><path d="M6.6 10.8a15.1 15.1 0 0 0 6.6 6.6l2.2-2.2a1 1 0 0 1 1-.25 11.4 11.4 0 0 0 3.6.57 1 1 0 0 1 1 1V20a1 1 0 0 1-1 1A17 17 0 0 1 3 4a1 1 0 0 1 1-1h3.5a1 1 0 0 1 1 1c0 1.25.2 2.45.57 3.57a1 1 0 0 1-.25 1z"/></svg>
        <span>555-014-2287</span>
      </div>
      <div class="contact-line">
        <svg viewBox="0 0 24 24" aria-hidden="true"><path d="M2 5h20v14H2z M2 5l10 8 10-8" /></svg>
        <span>ridgelinebuild@mail.com</span>
      </div>
    </div>
    <p class="licenses"><span class="licenses-label">Licenses :</span>VA 2701468352<span class="divider">|</span>NC 61845</p>
  </section>
</main>
</body>
</html>
```